new banner sliders for our web site

We would like to replace and create new set of sliding banners (5-10, resolution 930x380) for the main page of our online store at http://www.velomirt.example/online. We are thinking about highlighting the main company's products and services categories as well as maybe some featured individual products with those banners on the product pages.

1: Long Range Bluetooth® set of products showing off the super long range our our products as well as the capability to extend the range to normally 10m by factor 10 or more.
2: The product we have are used to connect industrial bar code scanners, GPS, land surveying instruments and other Bluetooth devices to a PC and greater range.
3: You can use our products to connect Bluetooth audio speakers to your PC or you can use e.g. the KORVENlink Tono QM to receive music from your smartphone to your home stereo system. Products can be used to connect keyboard/mouse in a home theater system, where the PC is in the basement, e.g.
4: A new category products is based on the Bluetooth Smart® standard. Making BLE (Bluetooth Low Energy) long range is unique. The products can be used for iBeacon transmission at higher power, the biggest in industry (GrandPulse) or it can be used to receive iBeacon transmissions, even relaying them. iBeacons are used for proximity marketing advertisement, allowing stores to reach more customers.
5: Long range BLE must be used to get data from heart rate sensors in a gym setting e.g. where you have a number of people wearing those in a large room. It could be a football game where players wear BLE sensors.
6: we have a set of Bluetooth to Serial products that can be highlighted in a banner: standard Bluetooth: Wirol7, Wirol7Q, Pico and Bluetooth Smart: TidyPico
7: another banner should highlight that all our products are build with our own Bluetooth modules (KORVENlink PVT, KORVENlink LUX). We are also offering custom product design and firmware development to meet customer's need. We know how to make modules and we can make one for you at any size and with any type of sensor attached to it.
8: last is a product we are developing for the home automation industry. We started with a web page at http://www.glowtuner.example, username korvenlink password korvenlink. A single banner that matches the other designs would be nice. This is an "available soon" product.

If you come up with other ideas how to highlight our products and services, we would be grateful and you have the winning bid.

Thank you very much
Torvald

The market for long range Bluetooth products is mostly industrial or B2B. E.g. our products are used with industrial sensors like barcode scanners in a warehouse or survey instruments in the field. They are also used by marketing companies who engage in the new iBeacon technology to reach customers at a greater instance.
Some customers are home automation companies or home theatre installers for long range mouse/keyboard connections or audio receiver at home stereo systems.
Our products are seldom used by the average consumer.

Industrial

Must have
• The banner design should visualize the use cases of our products. We'd like to see one or more banners for each use case that visualize:
1: long range capability, featuring Nodo QM or GrandPulse
2: industrial serial to computer connections, featuring Wirol7(Q) and TidyPico
3: proximity marketing, featuring KeenPulse and GrandPulse
4: custom design service, featuring KORVENlinkPVT and KORVENlinkLUX
5: home automation, featuring GlowTuner, TapSocket
6: home theatre, featuring Nodo QM and Tono QM
Nice to have
• Parallax and responsive
Should not have
• too much consumer oriented product presentation

```html
<!DOCTYPE html>
<html lang="en">
<head>
<meta charset="utf-8">
<title>Long Range Connections Banner</title>
<link rel="stylesheet" href="https://fonts.googleapis.com/css2?family=PT+Sans:ital,wght@1,400&display=swap">
<style>
  :root {
    --photo-light: #c9d3dd;
    --photo-mid: #8ea4bb;
    --photo-dark: #5d7591;
    --skin: #b99a86;
    --band-dark: #0b1a2e;
    --band-mid: #0f5a7e;
    --band-glow: #38e3f5;
    --ray: rgba(235, 250, 255, 0.85);
    --node-fill: #ffffff;
    --node-glow: rgba(80, 220, 255, 0.9);
    --icon: #111111;
    --text: #ffffff;
  }
  html, body {
    margin: 0;
    padding: 0;
    overflow: hidden;
    background: #ffffff;
  }
  .banner {
    position: relative;
    width: 1200px;
    height: 490px;
    overflow: hidden;
    font-family: "PT Sans", Arial, sans-serif;
  }
  .banner__photo {
    position: absolute;
    inset: 0;
    background:
      radial-gradient(ellipse 180px 220px at 870px 300px, rgba(185,154,134,0.55), transparent 70%),
      radial-gradient(ellipse 260px 300px at 600px 40px, rgba(230,215,200,0.55), transparent 70%),
      linear-gradient(90deg, var(--photo-dark) 0%, var(--photo-light) 30%, var(--photo-mid) 60%, var(--photo-light) 85%, var(--photo-mid) 100%);
  }
  .banner__network {
    position: absolute;
    inset: 0;
  }
  .banner__band {
    position: absolute;
    left: 0;
    top: 383px;
    width: 1200px;
    height: 107px;
    background:
      radial-gradient(ellipse 330px 140px at 600px 40px, var(--band-glow) 0%, rgba(56,227,245,0.65) 40%, transparent 100%),
      linear-gradient(90deg, var(--band-dark) 0%, var(--band-mid) 35%, var(--band-mid) 65%, var(--band-dark) 100%);
    box-shadow: 0 -6px 18px rgba(56, 227, 245, 0.45);
  }
  .banner__band::before {
    content: "";
    position: absolute;
    left: 0; right: 0; top: 0;
    height: 2px;
    background: linear-gradient(90deg, transparent, rgba(160,245,255,0.9) 30%, #ffffff 50%, rgba(160,245,255,0.9) 70%, transparent);
  }
  .banner__copy {
    position: absolute;
    top: 22px;
    margin: 0;
    color: var(--text);
    font-style: italic;
    font-weight: 400;
    font-size: 26px;
    line-height: 36px;
    letter-spacing: -0.3px;
    text-shadow: 0 1px 2px rgba(0,0,0,0.5);
  }
  .banner__copy--left { left: 36px; }
  .banner__copy--right { left: 716px; }
  .banner__brand {
    position: absolute;
    left: 0;
    width: 1200px;
    top: 38px;
    text-align: center;
    margin: 0;
    font-style: italic;
    font-size: 22px;
    color: #1d6f93;
    letter-spacing: 1px;
  }
</style>
</head>
<body>
<div class="banner">
  <div class="banner__photo" role="img" aria-label="Photo of a man in a light blue shirt reaching out to touch a floating network of device icons"></div>

  <svg class="banner__network" width="1200" height="490" viewBox="0 0 1200 490" xmlns="http://www.w3.org/2000/svg">
    <defs>
      <filter id="node-glow" x="-50%" y="-50%" width="200%" height="200%">
        <feGaussianBlur stdDeviation="6" result="b"/>
        <feMerge><feMergeNode in="b"/><feMergeNode in="SourceGraphic"/></feMerge>
      </filter>
    </defs>

    <g class="rays" stroke="var(--ray)" stroke-width="1.3" fill="none">
      <line x1="288" y1="58" x2="580" y2="400"/>
      <line x1="300" y1="62" x2="592" y2="400"/>
      <line x1="252" y1="155" x2="575" y2="400"/>
      <line x1="262" y1="160" x2="588" y2="400"/>
      <line x1="467" y1="226" x2="590" y2="400"/>
      <line x1="478" y1="226" x2="598" y2="400"/>
      <line x1="417" y1="329" x2="585" y2="400"/>
      <line x1="425" y1="336" x2="595" y2="400"/>
      <line x1="467" y1="226" x2="848" y2="97"/>
      <line x1="848" y1="97" x2="610" y2="400"/>
      <line x1="855" y1="100" x2="620" y2="400"/>
      <line x1="787" y1="265" x2="612" y2="400"/>
      <line x1="787" y1="265" x2="970" y2="219"/>
      <line x1="970" y1="219" x2="622" y2="400"/>
      <line x1="965" y1="226" x2="615" y2="400"/>
    </g>

    <g class="nodes" fill="var(--node-fill)" filter="url(#node-glow)">
      <circle cx="288" cy="58" r="34"/>
      <circle cx="252" cy="155" r="34"/>
      <circle cx="467" cy="226" r="34"/>
      <circle cx="417" cy="329" r="34"/>
      <circle cx="848" cy="97" r="34"/>
      <circle cx="787" cy="265" r="34"/>
      <circle cx="970" cy="219" r="34"/>
    </g>

    <g class="icons" fill="var(--icon)">
      <!-- car -->
      <path d="M270 64 l4 -14 q2 -5 7 -5 h14 q5 0 7 5 l4 14 q4 1 4 5 v8 h-5 v5 h-6 v-5 h-22 v5 h-6 v-5 h-5 v-8 q0 -4 4 -5z M276 63 h24 l-3 -11 h-18z"/>
      <circle cx="275" cy="70" r="3" fill="#fff"/>
      <circle cx="301" cy="70" r="3" fill="#fff"/>
      <!-- surveying instrument -->
      <path d="M234 142 l30 -10 l3 8 l-30 10z"/>
      <circle cx="252" cy="152" r="5"/>
      <path d="M251 155 l-12 22 h3 l10 -18 l10 18 h3 l-12 -22z"/>
      <rect x="250" y="156" width="3" height="20"/>
      <!-- laptop -->
      <rect x="451" y="211" width="32" height="21" rx="2"/>
      <rect x="455" y="215" width="24" height="14" fill="#fff"/>
      <path d="M446 234 h42 l-3 5 h-36z"/>
      <!-- phone -->
      <rect x="405" y="307" width="24" height="42" rx="4"/>
      <rect x="408" y="313" width="18" height="28" fill="#fff"/>
      <!-- headphones -->
      <path d="M828 104 q0 -28 20 -28 q20 0 20 28 h-5 q0 -22 -15 -22 q-15 0 -15 22z"/>
      <rect x="826" y="100" width="9" height="17" rx="3"/>
      <rect x="861" y="100" width="9" height="17" rx="3"/>
      <!-- handheld scanner -->
      <path d="M772 250 h28 q6 0 6 6 v6 q0 5 -6 5 h-8 l5 20 h-9 l-6 -20 h-10z"/>
      <!-- mouse -->
      <rect x="958" y="199" width="24" height="40" rx="12"/>
      <rect x="968" y="206" width="4" height="9" rx="2" fill="#fff"/>
    </g>
  </svg>

  <div class="banner__band">
    <p class="banner__copy banner__copy--left">Lorem ipsum dolor sit amet, consectetuer<br>adipiscing elit, sed diam nonummy.</p>
    <p class="banner__brand">ORBLINK</p>
    <p class="banner__copy banner__copy--right">Lorem ipsum dolor sit amet, consectetuer<br>adipiscing elit, sed diam nonummy.</p>
  </div>
</div>
</body>
</html>
```